Stroomwacht Powerpoint - presentation slides for energy management tool

We need a Powerpoint presentation lay-out which matches our logo from Stroomwacht.nl. 10 slides variations minimum, enough for a full professional presentation to potential clients.
Stroomwacht is a Dutch energymanagement tool for corporate real estate and housing agency. Our clients are Social houseing organisation, real estate owers, property managers and property developers.
Target Market(s)
real estate owners
Property manage
Font styles to use
Sans Serif
Colors
f78f20
0255a3
Requirements
Must have
- Stroomwacht logo colors and style
#F37122 orange
#00345D darkblue
Nice to have
- Professional look, background not white in every slide
Should not have
- wrong color orange and blue.

```html
<!DOCTYPE html>
<html lang="en">
<head>
<meta charset="utf-8">
<title>Stroomwacht Presentation Slides</title>
<link href="https://fonts.googleapis.com/css2?family=Bebas+Neue&family=Roboto:wght@400;500;700&family=Roboto+Condensed:wght@400;700&display=swap" rel="stylesheet">
<style>
:root{
  --orange:#F37122;
  --navy:#00345D;
  --blue:#0255a3;
  --cyan:#0aa6d6;
  --slide-bg:#f5f6f8;
  --rule:#e4e7eb;
  --ink:#222;
  --grey:#666;
}
*{margin:0;padding:0;box-sizing:border-box}
html,body{width:1200px;height:1200px;overflow:hidden}
body{background:linear-gradient(120deg,#e3eaf1 0%,#f2f5f8 55%,#fafbfc 100%);font-family:'Roboto',sans-serif;color:var(--ink);position:relative}
.slide{position:absolute;width:574px;height:322px;background:var(--slide-bg);transform:scale(.6202);transform-origin:0 0;overflow:hidden}
.slide *{position:absolute}
.header{left:0;top:0;width:574px;height:62px;background:#fff;border-bottom:1px solid var(--rule)}
.header .mark{left:14px;top:18px;width:24px;height:24px;border-radius:50%;background:var(--orange)}
.header h2{left:50px;top:19px;font-family:'Bebas Neue',sans-serif;font-weight:400;font-size:25px;letter-spacing:2px;color:var(--navy);white-space:nowrap}
.page-no{left:535px;top:0;width:26px;height:38px;background:var(--navy);color:#fff;font-size:10px;font-weight:700;display:flex;align-items:center;justify-content:center}
.small{font-size:7.5px;line-height:1.25;color:#333}
.body-text{font-size:9.5px;line-height:1.3;color:#333;text-align:justify}
.wordmark{font-family:'Bebas Neue',sans-serif;color:var(--navy);white-space:nowrap}
.brand-row *{position:static}
.brand-row{display:flex;align-items:center;gap:6px}
.brand-row .dot{width:20px;height:20px;border-radius:50%;background:var(--orange);flex:none}
.page-title{left:823px;top:40px;font-family:'Bebas Neue',sans-serif;font-weight:400;font-size:70px;line-height:.95;color:#111;position:absolute}
.toc-item{width:140px;height:60px}
.toc-item .tag{left:0;top:0;width:34px;height:18px;background:var(--navy);color:#fff;font-size:8px;padding:4px 0 0 6px}
.toc-item .chev{left:34px;top:0;width:0;height:0;border-top:9px solid transparent;border-bottom:9px solid transparent;border-left:10px solid var(--orange)}
.toc-item p{left:-2px;top:24px;width:140px}
.ico{width:18px;height:18px;border-radius:50%}
.tile{width:58px;height:58px;background:#fff;border:1px solid var(--rule);border-radius:3px}
.tile .glyph{left:19px;top:10px;width:20px;height:20px;border-radius:4px}
.tile span{left:2px;top:36px;width:52px;text-align:center;font-size:6px;line-height:1.2;color:var(--orange);font-weight:500}
.mtile{width:64px;height:64px;background:#fff;border:1px solid var(--rule);border-radius:4px}
.mtile .glyph{left:22px;top:10px;width:20px;height:20px;border-radius:50%;border:2px solid var(--orange)}
.mtile span{left:2px;top:40px;width:58px;text-align:center;font-size:6px;line-height:1.2;color:var(--orange)}
.stat b{display:block;position:static;font-size:20px;font-weight:700}
.stat i{display:block;position:static;font-style:normal;font-size:9px;font-weight:700;color:#222}
.stat em{display:block;position:static;font-style:normal;font-size:5px;line-height:1.3;color:#888;width:66px;margin-top:4px}
.curve-label{font-size:7px;color:var(--orange);white-space:nowrap}
.stage-label{font-size:7px;font-weight:700;color:#222;text-align:center;width:60px}
.stage-list{font-size:6.5px;line-height:1.3;color:#444;width:50px}
.point{width:150px;text-align:center}
.point .sq{position:relative;margin:0 auto;width:44px;height:44px;border-radius:4px;display:block}
.point h4{position:static;font-size:9px;font-weight:500;margin-top:14px;font-family:'Roboto Condensed',sans-serif}
.point p{position:static;font-size:7px;line-height:1.25;color:#444;margin-top:6px}
</style>
</head>
<body>

<h1 class="page-title">Presentation<br>Mockup</h1>

<section class="slide" style="left:422px;top:0;height:265px;background:#fff">
  <div class="brand-row" style="left:48px;top:88px;gap:8px">
    <span class="dot" style="width:76px;height:76px"></span>
    <span class="wordmark" style="font-size:78px;line-height:1">Stroomwacht</span>
  </div>
</section>

<section class="slide" style="left:422px;top:186px">
  <div class="header"><div class="mark"></div><h2>Table of Content</h2></div>
  <div class="page-no">2</div>
  <div class="toc-item" style="left:72px;top:100px"><div class="tag">01.</div><div class="chev"></div><p class="small">Contrary to popular belief, Lorem Ipsum is not simply random text.</p></div>
  <div class="toc-item" style="left:224px;top:100px"><div class="tag">02.</div><div class="chev"></div><p class="small">Contrary to popular belief, Lorem Ipsum is not simply random text.</p></div>
  <div class="toc-item" style="left:382px;top:100px"><div class="tag">03.</div><div class="chev"></div><p class="small">Contrary to popular belief, Lorem Ipsum is not simply random text.</p></div>
  <div class="toc-item" style="left:72px;top:192px"><div class="tag">04.</div><div class="chev"></div><p class="small">Contrary to popular belief, Lorem Ipsum is not simply random text.</p></div>
  <div class="toc-item" style="left:224px;top:192px"><div class="tag">05.</div><div class="chev"></div><p class="small">Contrary to popular belief, Lorem Ipsum is not simply random text.</p></div>
  <div class="toc-item" style="left:382px;top:192px"><div class="tag">06.</div><div class="chev"></div><p class="small">Contrary to popular belief, Lorem Ipsum is not simply random text.</p></div>
</section>

<section class="slide" style="left:22px;top:343px">
  <div class="header"><div class="mark"></div><h2>Summary of About Us</h2></div>
  <div class="page-no">3</div>
  <div style="left:0;top:98px;width:20px;height:145px;background:var(--orange)"></div>
  <div role="img" aria-label="Photo of a desktop computer and keyboard on a dark desk" style="left:20px;top:98px;width:223px;height:145px;background:linear-gradient(135deg,#2b2d30 0%,#6d7176 45%,#1a1b1d 100%)"></div>
  <p class="small" style="left:288px;top:105px;width:240px;font-size:7.8px">Aliquam erat risus, mattis non justo in, volutpat dictum diam. Aliquam sed dolor ac purus rutrum egestas. Maecenas sem eros, luctus quis facilisis in, tristique sit amet erat.</p>
  <div class="ico" style="left:285px;top:178px;background:var(--orange)"></div><p class="small" style="left:310px;top:180px">Cras at malesuada ipsum.<br>Ut vestibulum</p>
  <div class="ico" style="left:412px;top:178px;background:var(--blue)"></div><p class="small" style="left:443px;top:180px">Cras at malesuada ipsum.<br>Ut vestibulum</p>
  <div class="ico" style="left:285px;top:213px;background:var(--navy)"></div><p class="small" style="left:310px;top:215px">Cras at malesuada ipsum.<br>Ut vestibulum</p>
  <div class="ico" style="left:412px;top:213px;background:var(--cyan)"></div><p class="small" style="left:443px;top:215px">Cras at malesuada ipsum.<br>Ut vestibulum</p>
</section>

<section class="slide" style="left:422px;top:444px">
  <div class="header"><div class="mark"></div><h2>Global Market</h2></div>
  <div class="page-no">16</div>
  <div role="img" aria-label="World map highlighting North America, Europe, Africa and Asia" style="left:40px;top:108px;width:285px;height:160px;border-radius:40px;background:radial-gradient(ellipse at 25% 35%,#1d6fa3 0%,#1d6fa3 22%,transparent 40%),radial-gradient(ellipse at 52% 65%,#12a6dc 0%,#12a6dc 14%,transparent 28%),radial-gradient(ellipse at 50% 35%,#e85d24 0%,transparent 14%),radial-gradient(ellipse at 70% 40%,#b9b9b9 0%,#b9b9b9 30%,transparent 55%)"></div>
  <div style="left:337px;top:75px;width:1px;height:205px;background:#777"></div>
  <div class="stat" style="left:360px;top:96px"><b style="color:var(--orange)">15%</b><i>Europe</i><em>Short note on regional demand and growth.</em></div>
  <div class="stat" style="left:454px;top:96px"><b style="color:#333">30%</b><i>North America</i><em>Short note on regional demand and growth.</em></div>
  <div class="stat" style="left:360px;top:198px"><b style="color:var(--blue)">20%</b><i>Africa</i><em>Short note on regional demand and growth.</em></div>
  <div class="stat" style="left:454px;top:198px"><b style="color:var(--cyan)">35%</b><i>Asia</i><em>Short note on regional demand and growth.</em></div>
</section>

<section class="slide" style="left:822px;top:343px">
  <div style="left:0;top:130px;width:18px;height:96px;background:var(--navy)"></div>
  <div class="brand-row" style="left:48px;top:118px"><span class="dot"></span><span class="wordmark" style="font-size:22px">Stroomwacht</span></div>
  <h1 class="wordmark" style="left:48px;top:166px;font-size:30px;font-weight:400">Energy Management Tool</h1>
  <p style="left:48px;top:200px;font-size:13px;color:#222">Real-time Efficiencies, Real-time Results</p>
  <div style="left:46px;top:228px;width:262px;height:22px;background:var(--orange);color:#fff;font-size:10px;display:flex;align-items:center;justify-content:center">Presented by: Jan de Vries</div>
</section>

<section class="slide" style="left:22px;top:600px">
  <div class="header"><div class="mark"></div><h2>Interactive Media</h2></div>
  <div class="page-no">7</div>
  <p class="body-text" style="left:52px;top:85px;width:254px">The quick brown fox jumps over the lazy dog. The quick brown fox jumps over the lazy dog. The quick brown fox jumps over the lazy dog. The quick brown fox jumps over the lazy dog. The quick brown fox jumps over the lazy dog.</p>
  <div class="tile" style="left:47px;top:180px"><div class="glyph" style="background:var(--blue)"></div><span>ENHANCE USER ENGAGEMENT</span></div>
  <div class="tile" style="left:115px;top:180px"><div class="glyph" style="background:var(--cyan)"></div><span>RAISE BRAND AWARENESS</span></div>
  <div class="tile" style="left:184px;top:180px"><div class="glyph" style="background:#3aa372"></div><span>BOOST BRAND AFFINITY</span></div>
  <div class="tile" style="left:252px;top:180px"><div class="glyph" style="background:#e24a3b"></div><span>INCREASE ROI</span></div>
  <div role="img" aria-label="Desktop monitor showing a video player" style="left:352px;top:100px;width:180px;height:145px;border-radius:6px;background:linear-gradient(180deg,#2a2a2a 0%,#e8e8e8 8%,#e8e8e8 72%,#cfd2d5 100%)"></div>
</section>

<section class="slide" style="left:822px;top:600px">
  <div class="header"><div class="mark"></div><h2>Menu Icon</h2></div>
  <div class="page-no" style="left:538px">4</div>
  <h3 style="left:52px;top:97px;font-family:'Roboto Condensed',sans-serif;font-size:15px;color:#111">STROOMWACHT</h3>
  <p class="body-text" style="left:52px;top:128px;width:190px;font-size:8px;line-height:1.55">Aliquam erat risus, mattis non justo in, volutpat dictum diam. Aliquam sed dolor ac purus rutrum egestas. Maecenas sem eros, luctus quis facilisis in, tristique sit amet erat.</p>
  <div class="mtile" style="left:245px;top:84px"><div class="glyph"></div><span>BRAND AWARENESS</span></div>
  <div class="mtile" style="left:328px;top:84px"><div class="glyph" style="border-color:var(--cyan)"></div><span>SOCIAL INTEGRATION</span></div>
  <div class="mtile" style="left:411px;top:84px"><div class="glyph" style="border-color:#3aa372"></div><span>CONTEXTUAL RELEVANCY</span></div>
  <div class="mtile" style="left:494px;top:84px"><div class="glyph" style="border-color:#9a5a30"></div><span>DIRECT RESPONSE</span></div>
  <div class="mtile" style="left:245px;top:174px"><div class="glyph" style="border-color:var(--blue)"></div><span>CONSUMER ENGAGEMENT</span></div>
  <div class="mtile" style="left:328px;top:174px"><div class="glyph"></div><span>BRAND LIFT</span></div>
  <div class="mtile" style="left:411px;top:174px"><div class="glyph" style="border-color:#3aa372"></div><span>GEO FENCING</span></div>
  <div class="mtile" style="left:494px;top:174px"><div class="glyph" style="border-color:var(--navy)"></div><span>AUDIENCE VERTICAL TARGETING</span></div>
  <div style="left:0;top:258px;width:574px;height:64px;background:#fff">
    <p style="left:52px;top:6px;font-size:8.5px;font-weight:500">Trusted Partners:</p>
    <div style="left:54px;top:24px;width:46px;height:16px;border-radius:3px;background:#c9ced4"></div>
    <div style="left:118px;top:24px;width:68px;height:16px;border-radius:3px;background:#c9ced4"></div>
    <div style="left:204px;top:24px;width:92px;height:16px;border-radius:3px;background:#9aa1a8"></div>
  </div>
</section>

<section class="slide" style="left:422px;top:700px">
  <div class="header"><div class="mark"></div><h2>Product Maturity</h2></div>
  <div class="page-no">18</div>
  <svg style="left:0;top:0" width="574" height="200" viewBox="0 0 574 200">
    <path d="M31 185 Q70 178 95 160 L95 185 Z" fill="#0e3a66"/>
    <path d="M100 185 L100 157 Q130 140 150 100 L150 185 Z" fill="#1272a8"/>
    <path d="M155 185 L155 95 Q185 79 215 95 L215 185 Z" fill="#0fb0de"/>
    <path d="M220 185 L220 100 Q240 140 271 157 L271 185 Z" fill="#f37122"/>
    <path d="M276 185 L276 160 Q300 178 343 185 Z" fill="#0e3a66"/>
  </svg>
  <p class="curve-label" style="left:166px;top:73px">Pragmatists</p>
  <p class="curve-label" style="left:99px;top:114px">Visionaries</p>
  <p class="curve-label" style="left:234px;top:115px">Conservatives</p>
  <p class="curve-label" style="left:29px;top:148px">Tech Enthusiasts</p>
  <p class="curve-label" style="left:290px;top:155px">Skeptics</p>
  <p class="stage-label" style="left:33px;top:195px">Innovators</p>
  <p class="stage-label" style="left:95px;top:195px">Early Adopters</p>
  <p class="stage-label" style="left:155px;top:195px">Early Majority</p>
  <p class="stage-label" style="left:215px;top:195px">Late Majority</p>
  <p class="stage-label" style="left:280px;top:195px">Laggards</p>
  <p class="stage-list" style="left:43px;top:214px">• The quick,<br>&nbsp;&nbsp;brown<br>• Jumps over<br>&nbsp;&nbsp;a lazy</p>
  <p class="stage-list" style="left:104px;top:214px">• The quick,<br>&nbsp;&nbsp;brown<br>• Jumps over<br>&nbsp;&nbsp;a lazy</p>
  <p class="stage-list" style="left:169px;top:214px">• The quick,<br>&nbsp;&nbsp;brown<br>• Jumps over<br>&nbsp;&nbsp;a lazy</p>
  <p class="stage-list" style="left:234px;top:214px">• The quick,<br>&nbsp;&nbsp;brown<br>• Jumps over<br>&nbsp;&nbsp;a lazy</p>
  <p class="stage-list" style="left:301px;top:214px">• The quick,<br>&nbsp;&nbsp;brown<br>• Jumps over<br>&nbsp;&nbsp;a lazy</p>
  <p style="left:385px;top:112px;font-size:10px;font-weight:700;line-height:1.3">Product<br><span style="position:static;font-size:13px">Maturity</span></p>
  <div style="left:385px;top:145px;width:118px;height:2px;background:var(--navy)"></div>
  <p style="left:385px;top:155px;font-size:7.5px;font-weight:700">Phasellus maximus mauris.</p>
  <p class="body-text" style="left:385px;top:170px;width:170px;font-size:7px">Vivamus sollicitudin ac nisi non molestie. Aenean cursus, nisl volutpat vulputate commodo, ex lacus maximus dolor, et hendrerit odio velit eget augue. Integer vel lacinia lacus, ut auctor ante.</p>
</section>

<section class="slide" style="left:22px;top:857px">
  <div style="left:3px;top:88px;width:20px;height:36px;background:var(--orange)"></div>
  <h1 class="wordmark" style="left:45px;top:80px;font-size:50px;font-weight:400">Thank You</h1>
  <div class="brand-row" style="left:50px;top:140px"><span class="dot"></span><span class="wordmark" style="font-size:22px">Stroomwacht</span></div>
  <p style="left:50px;top:195px;font-family:'Roboto Condensed',sans-serif;font-size:14px;font-weight:700;color:#333">Jan de Vries</p>
  <p style="left:50px;top:213px;font-size:10px;color:#555">Vice President</p>
  <svg style="left:51px;top:234px" width="12" height="60" viewBox="0 0 12 60" fill="none" stroke="#444" stroke-width="1">
    <rect x="1" y="2" width="10" height="7"/><path d="M1 2 L6 6 L11 2"/>
    <path d="M2 19 Q2 26 9 27 L10 25 L8 23 L6 24 Q4 22 4 20 L5 18 L3 17 Z"/>
    <circle cx="6" cy="42" r="5"/><path d="M1 42 H11 M6 37 Q3 42 6 47 Q9 42 6 37"/>
  </svg>
  <p class="small" style="left:72px;top:235px;font-size:8px">jan@stroomwacht.nl</p>
  <p class="small" style="left:72px;top:253px;font-size:8px">(555) 010-2040</p>
  <p class="small" style="left:72px;top:272px;font-size:8px">www.stroomwacht.nl</p>
</section>

<section class="slide" style="left:822px;top:857px">
  <div style="left:5px;top:88px;width:19px;height:36px;background:var(--navy)"></div>
  <div class="brand-row" style="left:44px;top:92px"><span class="dot"></span><span class="wordmark" style="font-size:22px">Stroomwacht</span></div>
  <h1 class="wordmark" style="left:46px;top:130px;font-size:38px;font-weight:400;line-height:.95">The Section<br>Slide</h1>
</section>

<section class="slide" style="left:422px;top:956px">
  <div class="header"><div class="mark"></div><h2>3 Point &amp; Paragraph</h2></div>
  <div class="page-no" style="left:532px">6</div>
  <p style="left:52px;top:68px;width:460px;font-size:7.8px;line-height:1.3;color:#333">The quick brown fox jumps over the lazy dog. The quick brown fox jumps over the lazy dog. The quick brown fox jumps over the lazy dog. The quick brown fox jumps over the lazy dog. The quick brown fox jumps over the lazy dog. The quick brown fox jumps over the lazy dog.</p>
  <div class="point" style="left:56px;top:108px"><span class="sq" style="background:var(--navy)"></span><h4>Geographically Targeted</h4><p>The quick brown fox jumps over the lazy dog. The quick brown fox jumps over the lazy dog.</p></div>
  <div class="point" style="left:214px;top:108px"><span class="sq" style="background:var(--blue)"></span><h4>Consumer Profile Targeting</h4><p>The quick brown fox jumps over the lazy dog. The quick brown fox jumps over the lazy dog.</p></div>
  <div class="point" style="left:369px;top:108px"><span class="sq" style="background:var(--orange)"></span><h4>Audience &amp; Data Solutions</h4><p>The quick brown fox jumps over the lazy dog. The quick brown fox jumps over the lazy dog.</p></div>
  <div style="left:4px;top:208px;width:566px;height:22px;background:var(--orange);color:#fff;font-size:9.5px;display:flex;align-items:center;justify-content:center">Our Global Reach: +2.5 Billion Monthly</div>
  <p style="left:0;top:238px;width:574px;text-align:center;font-family:'Roboto Condensed',sans-serif;font-size:9px;font-weight:700">We Know:</p>
  <p style="left:52px;top:256px;width:460px;font-size:7.8px;line-height:1.3;color:#333">The quick brown fox jumps over the lazy dog. The quick brown fox jumps over the lazy dog. The quick brown fox jumps over the lazy dog. The quick brown fox jumps over the lazy dog. The quick brown fox jumps over the lazy dog. The quick brown fox jumps over the lazy dog.</p>
</section>

</body>
</html>
```